Lantern Dental Brochure

Most of the information is on the existing brochure, I just think the layout needs to be cleaner and more modern. I tend to like a darker brochure with white or light grey text (it also looks great with our new logo - also attached). The finished brochure should been in a format that I can send to pressly hub and also edit myself if the text needs to change.

Besides the info in the attached scan, I'd also like to include at-home custom fit whitening kits for $89. I am also looking for a new motto. It is currently "Quality Dentistry, Affordable Prices"

The web address has been changed to LanternDentalOzark.com and the email address is Info@LanternDentalOzark.com

I'd like to re-draw the maps as well. Our Hot Springs location is here:

https://www.mapfinder.example/place/5837+Birchwood+Ln,+Hot+Springs+National+Park,+AR+71999/@34.100000,-93.100000,17z/data=!3m1!4b1!4m2!3m1!1s0x0000000000000001:0x0000000000000002

Little Rock location:

https://www.mapfinder.example/place/48305+Marrow+Pike+Rd+%234400,+Little+Rock,+AR+72299/@34.7000000,-92.400000,17z/data=!3m1!4b1!4m2!3m1!1s0x0000000000000003:0x0000000000000004

Target Market(s)

Anyone who is interested in general dentistry except for young children. We currently see a lot of low income patients and retirees. We would like to expand that market.

Industry/Entity Type

Dental

Font styles to use
Other font styles liked:
• I don't know the name of the font but I like the one used in the logo

Requirements
Must have
• A catchy design - especially on the front page. We want people to pick them up and browse.
Nice to have
• I love ultra modern design. Minimalist. Sleek.
Should not have
• clashing colors like the current brochure. We're going for catchy but not cheezy.

```html
<!DOCTYPE html>
<html lang="en">
<head>
<meta charset="utf-8">
<title>Lantern Dental Brochure – Inside Spread</title>
<link rel="stylesheet" href="https://fonts.googleapis.com/css2?family=Arimo:wght@400;700&display=swap">
<style>
  :root {
    --page-bg: #5f6164;
    --silver-top: #e2e3e5;
    --silver-mid: #b4b6ba;
    --silver-low: #8e9094;
    --bronze: #8a7660;
    --bronze-deep: #6e5c48;
    --accent-blue: #3d8fc2;
    --accent-blue-dark: #2f7aab;
    --ink-dark: #1f1f21;
    --ink-bar: #2a2a2c;
    --text-light: #ffffff;
    --text-soft: #f1f2f4;
    --logo-box: #f3f4f6;
    --photo-a: #d8e6ea;
    --photo-b: #9fbfc6;
  }
  * { box-sizing: border-box; margin: 0; padding: 0; }
  html, body { width: 1200px; height: 900px; overflow: hidden; }
  body {
    background: var(--page-bg);
    font-family: "Arimo", Arial, sans-serif;
    color: var(--text-light);
  }
  .spread {
    position: absolute;
    left: 65px; top: 40px;
    display: flex; gap: 10px;
  }
  .panel {
    position: relative;
    width: 350px; height: 820px;
    background: linear-gradient(180deg, var(--silver-top) 0%, var(--silver-mid) 45%, var(--silver-low) 100%);
    overflow: hidden;
  }
  .panel--services {
    background: linear-gradient(180deg, var(--silver-top) 0%, var(--silver-mid) 55%, var(--silver-low) 100%);
  }
  .panel--partials {
    background: linear-gradient(180deg, var(--silver-top) 0%, var(--silver-mid) 30%, var(--bronze) 75%, var(--bronze-deep) 100%);
  }

  /* brand block */
  .brand {
    margin: 22px 22px 0;
    height: 118px;
    background: var(--logo-box);
    display: flex; align-items: center; justify-content: center; gap: 12px;
  }
  .brand__mark { width: 16px; height: 16px; background: var(--accent-blue); border-radius: 50%; }
  .brand__name {
    font-size: 30px; font-weight: 700; letter-spacing: 1px;
    color: var(--ink-dark); text-transform: uppercase;
  }

  .section-title {
    background: var(--ink-bar);
    color: var(--text-light);
    font-size: 22px; font-weight: 700;
    text-align: center;
    padding: 9px 0;
    margin: 14px 0 0;
  }

  .price-table {
    width: 100%;
    background: var(--ink-bar);
    border-collapse: collapse;
    font-size: 11px;
  }
  .price-table th, .price-table td { padding: 2px 22px; text-align: left; font-weight: 400; }
  .price-table tr:last-child td { padding-bottom: 10px; }

  .tier { margin-top: 10px; }
  .tier__label, .item__label {
    background: var(--accent-blue);
    color: var(--text-light);
    font-size: 12px; font-weight: 700;
    padding: 5px 22px;
  }
  .tier__text, .item__text {
    font-size: 10.5px; line-height: 1.45;
    padding: 6px 22px 0;
    color: var(--text-soft);
  }

  .photo {
    position: absolute; left: 0; right: 0; bottom: 0; height: 230px;
    background: linear-gradient(135deg, var(--photo-a), var(--photo-b));
  }

  /* services panel */
  .services__visual {
    margin: 22px 22px 0; height: 120px;
    background: linear-gradient(135deg, #7b7e83, #4e5155);
  }
  .item { margin-top: 12px; }
  .services__note {
    position: absolute; left: 22px; right: 22px; bottom: 70px;
    font-size: 10.5px; line-height: 1.5; color: var(--text-soft);
  }
  .services__band {
    position: absolute; left: 0; right: 0; bottom: 0; height: 40px;
    background: var(--accent-blue-dark);
  }

  /* partials panel */
  .panel--partials .section-title { margin-top: 22px; }
  .warranty {
    margin: 18px 22px 0;
    background: var(--ink-dark);
    font-size: 10.5px; line-height: 1.5;
    padding: 14px 16px;
    color: var(--text-soft);
  }
  .web {
    position: absolute; left: 0; right: 0; bottom: 26px;
    text-align: center; font-size: 12px; letter-spacing: 0.5px;
  }
</style>
</head>
<body>
<main class="spread">

  <section class="panel panel--dentures">
    <div class="brand">
      <span class="brand__mark"></span>
      <span class="brand__name">Lantern Dental</span>
    </div>
    <h2 class="section-title">Dentures</h2>
    <table class="price-table">
      <tr><th></th><th>Full Set</th><th>Upper or Lower</th></tr>
      <tr><td>Standard</td><td>$800</td><td>$450</td></tr>
      <tr><td>Premium</td><td>$1200</td><td>$650</td></tr>
      <tr><td>Elite</td><td>$1600</td><td>$850</td></tr>
    </table>
    <div class="tier">
      <p class="tier__label">Standard - Most Economical</p>
      <p class="tier__text">The dentist and lab technician select the size, shape and color of the teeth. A functioning denture with a medium tooth shade.</p>
    </div>
    <div class="tier">
      <p class="tier__label">Premium - Cosmetic Approval</p>
      <p class="tier__text">The Premium denture teeth are set in wax for the patient to approve at a Wax Try-In, so you can preview the look before final fabrication. This denture comes in 3 tooth shades.</p>
    </div>
    <div class="tier">
      <p class="tier__label">Elite - Most Popular</p>
      <p class="tier__text">The Elite dentures use a higher quality tooth which gives you a longer wear and a more natural look. It includes a Wax Try-In for cosmetic approval and a broad choice of tooth shades, including the B-1 (Extremely White) shade as well as ethnic tinting of gums.</p>
    </div>
    <div class="photo" role="img" aria-label="Photo of a smiling patient in the dental chair with a dentist at work"></div>
  </section>

  <section class="panel panel--services">
    <div class="services__visual" role="img" aria-label="Photo of a dental treatment room"></div>
    <div class="item">
      <p class="item__label">Cleanings &amp; Exams</p>
      <p class="item__text">Routine cleanings, x-rays and full exams to keep your smile healthy year round.</p>
    </div>
    <div class="item">
      <p class="item__label">Fillings &amp; Extractions</p>
      <p class="item__text">Tooth colored fillings and gentle extractions done in one visit when possible.</p>
    </div>
    <div class="item">
      <p class="item__label">Relines &amp; Repairs</p>
      <p class="item__text">Same day denture repairs and relines to restore a comfortable fit.</p>
    </div>
    <div class="item">
      <p class="item__label">Whitening Kits - $89</p>
      <p class="item__text">At-home custom fit whitening trays with professional gel.</p>
    </div>
    <p class="services__note">Call or visit either of our offices to schedule your appointment today.</p>
    <div class="services__band"></div>
  </section>

  <section class="panel panel--partials">
    <h2 class="section-title">Partial Dentures</h2>
    <div class="item">
      <p class="item__label">Acrylic Partials (Flippers) - $300/arch</p>
      <p class="item__text">Basic partial replacing up to 3 teeth. Must be worn as a temporary.</p>
    </div>
    <div class="item">
      <p class="item__label">Acrylic Partials w/clasps - $450/arch</p>
      <p class="item__text">Replacing all missing teeth in arch with wire clasps to hold partial in place. Most affordable replacement of missing teeth.</p>
    </div>
    <div class="item">
      <p class="item__label">Cast Metal Partials - $900/arch</p>
      <p class="item__text">Stronger and less bulky and offers a better fit. Metal framework with metal clasps (not wire). Takes 2-3 weeks.</p>
    </div>
    <div class="item">
      <p class="item__label">Flexible Partials - $1100</p>
      <p class="item__text">A comfortable tissue supported partial that shows no clasps. Recommended for cosmetic purposes and periodontally involved teeth. (2-3 weeks)</p>
    </div>
    <div class="item">
      <p class="item__label">Clear Clasp Partials - $1300</p>
      <p class="item__text">A more esthetically pleasing alternative to cast metal partials. For people who desire a tight fitting partial and have sound tooth and bone. (2-3 weeks)</p>
    </div>
    <p class="warranty">All permanent dentures come with a one year warranty that covers defects in materials and workmanship. All dentures and partials are made with NDC (National Dental Council) approved teeth. All dentures and partials are made with Corvane Hi-Impact acrylic base (gum) material which ensures the greatest protection against breakage.</p>
    <p class="web">www.LanternDentalOzark.com</p>
  </section>

</main>
</body>
</html>
```